Design a menu for health restaurant

A health food restaurant in Los Angeles is seeking menu design. Our foods are made from scratch using whole ingredients.
Name: Grubb Larder
Address: 1000 E 60th StLos Angeles, CA 90247
Website: www.GrubbLarder.example
We are looking for a clean and simple menu. Brand colors are white/tan, green and orange.

Please see attached excel with menu items and logo. We do not yet have prices.

Colors
f78f20
9bcb3c
ffffff
fff3d1

Requirements
Must have
• Easy to read.
Trifold menu design (front and back).
VEGAN, VEGETARIAN, GLUTEN FREE, CONTAINS NUTS symbols.
Logo.
Nice to have
• Incorporate brand colors, but still be easy to read.
We would like to use the Belco font (attached) if it works. If not we are open to a similar font that is easy to read.

Please see attached images.
We like the images and headers of OPTION 1. Would like something similar in trifold format.
We like the clean fonts of OPTION 2.

```html
<!DOCTYPE html>
<html lang="en">
<head>
<meta charset="utf-8">
<title>Grubb Larder Menu</title>
<link href="https://fonts.googleapis.com/css2?family=Alegreya:ital,wght@0,400;0,500;1,400&family=Barlow:ital,wght@0,400;0,500;1,300&display=swap" rel="stylesheet">
<style>
:root{
  --teal:#9ccccc;
  --green:#5f9a63;
  --green-band:#6a9a64;
  --ink:#333;
  --paper:#f2f2f2;
  --slate:#3a3d3f;
  --orange:#ef6f23;
  --pale-teal:#a9d4d4;
}
*{margin:0;padding:0;box-sizing:border-box}
html,body{width:1200px;height:933px;overflow:hidden;background:#fff}
.canvas{position:relative;width:1200px;height:933px;background:#fff;font-family:'Barlow',sans-serif;color:var(--ink)}
.inside{position:absolute;left:13px;top:13px;width:782px;height:907px;background:var(--paper)}
.cover{position:absolute;left:795px;top:13px;width:394px;height:907px;background:var(--slate)}
.section-head{position:absolute;height:31px;background:var(--teal);border-top-right-radius:30px 31px;font-family:'Alegreya',serif;font-style:italic;font-size:23px;line-height:31px;padding-left:12px;color:#1f2a2a}
.item{position:absolute}
.col-left .item{left:44px;width:331px}
.col-mid .item{left:420px;width:327px}
.name{font-weight:500;font-size:12px;color:var(--green);line-height:14px;height:14px;display:flex;align-items:center;gap:5px;white-space:nowrap}
.price{position:absolute;right:0;top:0;font-size:11.5px;line-height:14px;font-weight:500;color:var(--green)}
.desc{font-style:italic;font-weight:300;font-size:9px;line-height:11.6px;color:var(--ink);white-space:nowrap}
.tag{display:inline-flex;width:10px;height:10px;align-items:center;justify-content:center;font-size:5px;font-style:normal;color:#444;border:0.8px solid #444}
.tag.round{border-radius:50%}
.tag.diamond{transform:rotate(45deg);width:8px;height:8px}
.tag.diamond span{transform:rotate(-45deg)}
.photo{position:absolute;border:3px solid var(--green-band)}
.legend{position:absolute;left:98px;top:897px;width:570px;height:23px;background:var(--green-band);border-top-left-radius:22px 23px;border-top-right-radius:22px 23px;display:flex;align-items:center;justify-content:space-around;font-family:'Alegreya',serif;font-size:10px;color:#fff}
.legend span{display:flex;align-items:center;gap:5px}
.legend .tag{color:#fff;border-color:#fff}
.brand-seal{position:absolute;left:879px;top:248px;width:226px;height:226px;border-radius:50%;background:#fff;border:3px solid var(--orange);display:flex;align-items:center;justify-content:center;text-align:center;font-family:'Alegreya',serif;font-size:30px;line-height:1.05;color:var(--orange)}
.url-band{position:absolute;left:850px;top:496px;width:288px;height:19px;background:var(--green-band);border-top-left-radius:10px 19px;border-top-right-radius:14px 19px;text-align:center;font-family:'Alegreya',serif;font-style:italic;font-weight:500;font-size:11.5px;line-height:19px;color:#d8ecec}
.address{position:absolute;left:795px;top:543px;width:394px;text-align:center;font-family:'Alegreya',serif;font-size:22px;line-height:30px;color:var(--pale-teal)}
.phone{position:absolute;left:795px;top:612px;width:394px;text-align:center;font-family:'Alegreya',serif;font-weight:500;font-size:32px;color:var(--pale-teal)}
.social-band{position:absolute;left:797px;top:782px;width:241px;height:62px;background:var(--green-band);border-top-right-radius:50px 62px}
.social-dot{position:absolute;background:#fff}
</style>
</head>
<body>
<div class="canvas">
  <div class="inside"></div>
  <div class="cover"></div>

  <div class="col-left">
    <div class="section-head" style="left:32px;top:29px;width:352px">Burgers N’ Summies</div>
    <div class="item" style="top:72px"><div class="name">Air Fried Chicken Sammy</div><div class="price">11.99</div><div class="desc">Air fried chicken breast topped with red leaf lettuce, tomato,<br>house made pickles and Larder Sauce on a bun served with<br>choice of salad of fries.</div></div>
    <div class="item" style="top:126px"><div class="name">Grilled Chicken Sammy</div><div class="price">11.99</div><div class="desc">Grilled chicken topped with guacamole, red leaf lettuce,<br>tomato, house made pickles and Larder Sauce.<br>Served with regular fries or side salad.</div></div>
    <div class="item" style="top:179px"><div class="name">Classic Beef Burger</div><div class="price">11.99</div><div class="desc">House seasoned beef burger topped with red leaf lettuce,<br>tomato, cheddar cheese, house made pickles and Larder Sauce<br>on a bun served with choice of salad of fries.</div></div>
    <div class="item" style="top:234px"><div class="name">Black Bean Pine Nut Burger <i class="tag">V+</i><i class="tag round">GF</i></div><div class="price">11.99</div><div class="desc">House made black bean pine nut burger topped with red leaf<br>lettuce, tomato, house made pickles and mustard aioli<br>on a bun served with choice of salad of fries.</div></div>
    <div class="item" style="top:287px"><div class="name">Salmon Burger</div><div class="price">11.99</div><div class="desc">House made salmon burger topped with red leaf lettuce, tomato,<br>house made pickles and Larder yogurt on a bun served<br>with choice of salad of fries.</div></div>
    <div class="photo" role="img" aria-label="Photo of a grilled chicken sandwich with lettuce and guacamole" style="left:81px;top:345px;width:253px;height:138px;background:linear-gradient(160deg,#f4f2ee 0%,#c98a3a 35%,#6fa63a 60%,#e9e6df 100%)"></div>

    <div class="section-head" style="left:32px;top:500px;width:352px">Drinks</div>
    <div class="item" style="top:549px"><div class="name">Coffee</div><div class="desc">We proudly serve Bellwood Coffee, a local roaster.</div></div>
    <div class="item" style="top:578px"><div class="name">Power Date Shake</div><div class="desc">Ice-blended energy smoothie featuring dates<br>and coffee.</div></div>
    <div class="item" style="top:618px"><div class="name">Heart Beet Juice</div><div class="desc">Red beet, apple, carrot, ginger, parsley, and lemon.</div></div>
    <div class="item" style="top:647px"><div class="name">Green Leafy Juice</div><div class="desc" style="margin-top:2px">Spinach, kale, cucumber, apple, and oranges.</div></div>
    <div class="item" style="top:675px"><div class="name">Orange Turmeric Juice</div><div class="desc">Turmeric, ginger, lemon, carrot, and orange topped<br>with cracked black pepper.</div></div>
    <div class="item" style="top:714px"><div class="name">Fireshot</div><div class="desc">Ginger and lemon shot topped with cayenne.</div></div>
    <div class="item" style="top:742px"><div class="name">Lemonade</div><div class="desc">House Made Lemonade. Choice of unsweetened or agave sweetened in Regular,<br>Raspberry, and Lavender flavors.</div></div>
    <div class="item" style="top:783px"><div class="name">Tea</div><div class="desc">Hot or iced.</div></div>
    <div class="item" style="top:810px"><div class="name">Bottled Drinks</div><div class="desc">Tidewell kombucha (Trio Blend, Ginger Berry, Mango Glow)<br>Fizzline (Orange Mango, Lemon, Grapefruit)<br>Palmora Original<br>Sparkling Water (Clearspring)<br>Still Water (Clearspring)</div></div>
    <div class="photo" role="img" aria-label="Photo of a raspberry lemonade in a clear cup" style="left:248px;top:551px;width:129px;height:175px;background:linear-gradient(180deg,#f3e6e8 0%,#f26f80 45%,#f5a2a8 80%,#eceae6 100%)"></div>
  </div>

  <div class="col-mid">
    <div class="section-head" style="left:404px;top:29px;width:352px">Combos</div>
    <div class="item" style="top:74px"><div class="name">Soup + Salad</div><div class="price">11.99</div><div class="desc" style="margin-top:3px">Your choice of soup and side salad.<br>16oz soup + 38oz salad</div></div>
    <div class="item" style="top:120px"><div class="name">Avo Toast Combo</div><div class="price">11.99</div><div class="desc" style="margin-top:1px">Half avocado toast and your choice of soup. 16oz</div></div>
    <div class="item" style="top:152px"><div class="name">Soup + Sammy</div><div class="price">11.99</div><div class="desc" style="margin-top:3px">Your choice of soup and sandwich.<br>16oz soup + Sandwich</div></div>

    <div class="section-head" style="left:404px;top:215px;width:352px">Desserts</div>
    <div class="item" style="top:259px"><div class="name">Date Coffee Cake <i class="tag">V+</i><i class="tag round">N+</i></div><div class="price">11.99</div><div class="desc">Signature date coffee cake with walnuts.</div></div>
    <div class="item" style="top:289px"><div class="name">Fruit + Spices <i class="tag">V+</i><i class="tag round">GF</i></div><div class="price">11.99</div><div class="desc">Strawberry, pineapple, green apple, orange,<br>and blueberries with lime and chili seasoning.</div></div>
    <div class="item" style="top:331px"><div class="name">Cookies <i class="tag diamond"><span>V</span></i></div><div class="price">11.99</div><div class="desc">Your choice of Chocolate Chip or Double Chocolate<br>Chip fresh baked cookie.</div></div>
    <div class="item" style="top:373px"><div class="name">Larder Chocolate Mousse <i class="tag">V+</i><i class="tag round">GF</i></div><div class="price">11.99</div><div class="desc">Served with grated dark chocolate.</div></div>
    <div class="photo" role="img" aria-label="Photo of two cookies, double chocolate and chocolate chip" style="left:438px;top:409px;width:289px;height:118px;background:linear-gradient(90deg,#e8e8e6 0%,#5a3b2e 30%,#d9b97a 65%,#ececea 100%)"></div>

    <div class="section-head" style="left:404px;top:545px;width:352px">Snacks N’ Slides</div>
    <div class="item" style="top:594px"><div class="name">Fries <i class="tag">V+</i><i class="tag round">GF</i></div><div class="price">11.99</div><div class="desc" style="margin-top:2px">Hand cut air-fries with house seasonings.<br>Choose regular or sweet potato fries.</div></div>
    <div class="item" style="top:640px"><div class="name">Side Salad</div><div class="price">11.99</div><div class="desc">Your choice of House, Golden Beet,<br>Mediterranean, or Vegan Chef<br>side salad. (24oz)</div></div>
    <div class="item" style="top:697px"><div class="name">Guac + Chips</div><div class="price">11.99</div><div class="desc" style="margin-top:3px">Guacamole with blue corn tortilla chips.</div></div>
    <div class="item" style="top:731px"><div class="name">Hummus + Chips</div><div class="price">11.99</div><div class="desc" style="margin-top:2px">Hummus with blue corn tortilla chips.</div></div>
    <div class="photo" role="img" aria-label="Photo of guacamole with blue corn tortilla chips" style="left:439px;top:771px;width:290px;height:104px;background:linear-gradient(100deg,#3f3a4a 0%,#5a5566 25%,#c8d48a 50%,#ececea 75%,#f0e4dc 100%)"></div>
  </div>

  <div class="legend">
    <span><i class="tag diamond"><span>V</span></i> Vegetarian</span>
    <span><i class="tag round">GF</i> Gluten Free</span>
    <span><i class="tag">V+</i> Vegan</span>
    <span><i class="tag round">N+</i> Contains Nuts</span>
  </div>

  <div class="brand-seal">Grubb<br>Larder</div>
  <div class="url-band">www.GrubbLarder.example</div>
  <div class="address">2417 W 83rd St #18<br>Los Angeles CA 90247</div>
  <div class="phone">(555) 014-2290</div>
  <div class="social-band"></div>
  <div class="social-dot" style="left:874px;top:788px;width:48px;height:48px;border-radius:50%"></div>
  <div class="social-dot" style="left:944px;top:790px;width:46px;height:46px;border-radius:9px"></div>
</div>
</body>
</html>
```